依頼詳細
インターネット通販の本格的な正統派バレエショップ(ヨーロッパ風)を目指していますので、それに合うデザインと同時に、色のレギュレーションなどを決めてプロっぽいホームページを作りたいと思っています。
現在のホームページは色々な色があり、色のレギュレーションが出来ていませんので、今回のリニューアルと同時にメインカラー、ザブカラー、アクセントカラーなどを決めてプロっぽいページ作成をする為に依頼をしました。

既にロゴは決めているので、添付したロゴの色とイメージに合わせて作って下さい。

サイトURL
www.kiravostore.com
ページ数
1ページ
希望イメージ
シンプル 複雑
単色 カラフル
暗い 明るい
日常 高級
遊び心 厳粛
未来的 伝統的
女性的 男性的
希望する色
紫系、白のベースカラーにロゴ色である藤色をサブカラーと考えています。
納品ファイル
• イラストレーター形式 (.ai)
• フォトショップ形式 (.psd)
補足説明
ロゴを添付しました。
上部分の看板についてですが、添付しました看板を参考にお願いします。
現在のページですと看板が高く下にスクロールをしないと情報が見れないので、
直にわかるように看板を縦に短くしたいです。

報告が遅くなり大変申し訳ございませんでした。
■ 選んだ理由

ターゲットの年齢層にマッチしたデザインと、色使いがとても気に入りました。

■ 提案者全員のお礼・コメント

沢山の方がデザインをして下さり大変嬉しく思います。本当にありがとうございました。

```html
<!DOCTYPE html>
<html lang="ja">
<head>
<meta charset="utf-8">
<title>Kiravo バレエ用品通販</title>
<link href="https://fonts.googleapis.com/css2?family=Noto+Sans+JP:wght@400;700&family=Playfair+Display:ital,wght@0,400;0,700;1,400&display=swap" rel="stylesheet">
<style>
:root{
  --purple:#5a4777;
  --purple-dark:#3f3257;
  --lilac:#b6a2cb;
  --lilac-soft:#e9e2f0;
  --lilac-pale:#f6f3f9;
  --pink:#d9487d;
  --orange:#f08a3c;
  --ink:#3a3340;
  --muted:#8a8290;
  --line:#d9d2e0;
  --page:#f2f0f4;
  --white:#fff;
}
*{box-sizing:border-box;margin:0;padding:0}
html,body{width:1200px;height:4280px;overflow:hidden}
body{background:var(--page);font-family:"Noto Sans JP",sans-serif;color:var(--ink);font-size:12px;line-height:1.5;position:relative}
.serif{font-family:"Playfair Display",serif}
ul{list-style:none}

/* header */
.header{position:absolute;top:0;left:0;width:1200px;height:68px;background:var(--white);border-bottom:1px solid var(--line)}
.header .tagline{position:absolute;left:72px;top:4px;font-size:10px;color:var(--muted)}
.brand{position:absolute;left:72px;top:20px;display:flex;align-items:center;gap:8px;font-size:28px;font-weight:700;color:var(--purple);font-family:"Noto Sans JP",sans-serif}
.brand .dot{width:14px;height:14px;border-radius:50%;background:var(--lilac)}
.header .hours{position:absolute;left:470px;top:8px;font-size:10px;color:var(--muted);width:170px;line-height:1.4}
.phone{position:absolute;left:650px;top:16px;display:flex;align-items:center;gap:8px;font-size:30px;font-weight:700;color:var(--purple-dark);letter-spacing:1px}
.header .util{position:absolute;right:72px;top:6px;font-size:10px;color:var(--muted)}
.btn-shop{position:absolute;right:72px;top:28px;width:170px;height:30px;border-radius:3px;background:var(--pink);color:#fff;font-size:12px;font-weight:700;display:flex;align-items:center;justify-content:center}
.btn-cart{position:absolute;right:252px;top:28px;width:150px;height:30px;border:1px solid var(--line);border-radius:3px;font-size:12px;display:flex;align-items:center;justify-content:center;color:var(--purple)}

/* hero */
.hero{position:absolute;top:68px;left:0;width:1200px;height:372px;background:linear-gradient(100deg,#cfc6cf 0%,#eae4e6 35%,#f7f4f2 55%,#d8cfd3 80%,#b7aab6 100%)}
.hero h1{position:absolute;left:72px;top:80px;font-size:30px;font-weight:700;color:#fff;text-shadow:0 1px 3px rgba(60,40,80,.5)}
.hero p{position:absolute;left:72px;top:130px;font-size:14px;color:#fff;line-height:1.7;text-shadow:0 1px 2px rgba(60,40,80,.5)}

/* nav */
.gnav{position:absolute;top:440px;left:0;width:1200px;height:48px;background:linear-gradient(#fff,#e6e1ea);border-top:1px solid var(--line);border-bottom:1px solid var(--line)}
.gnav ul{display:flex;margin-left:72px;width:1056px;height:100%}
.gnav li{flex:1;display:flex;align-items:center;justify-content:center;font-size:13px;color:var(--purple-dark);border-right:1px solid var(--line)}
.gnav li:first-child{border-left:1px solid var(--line)}

/* sidebar */
.side{position:absolute;top:508px;left:72px;width:268px;display:flex;flex-direction:column;gap:14px}
.box{background:var(--white);border:1px solid var(--line)}
.box-head{height:30px;background:var(--purple);color:#fff;font-size:13px;font-weight:700;display:flex;align-items:center;padding:0 10px;justify-content:space-between}
.box-head small{font-size:9px;font-weight:400;opacity:.8}
.box-body{padding:10px}
.field{height:22px;border:1px solid var(--line);background:#fff;margin:4px 0;font-size:10px;color:var(--muted);padding:2px 6px}
.row-label{font-size:10px;color:var(--muted)}
.btn-sm{height:24px;background:var(--lilac);color:#fff;font-size:11px;display:flex;align-items:center;justify-content:center;border-radius:2px;margin-top:6px}
.link-sm{font-size:10px;color:var(--purple);margin-top:6px}
.promo{border:1px solid var(--line);display:flex;flex-direction:column;justify-content:center;padding:12px 14px}
.promo.member{height:110px;background:linear-gradient(#fff,#fde9ef)}
.promo.member b{font-size:22px;color:var(--pink)}
.promo.member span{font-size:13px;color:var(--ink)}
.promo.staff{height:130px;background:linear-gradient(90deg,#fff 55%,#ddd2e3);position:relative}
.promo.staff b{font-size:21px;color:var(--purple-dark);line-height:1.3}
.promo.staff span{font-size:12px;color:var(--pink)}
.promo.staff .img{position:absolute;right:0;top:0;width:100px;height:100%;background:linear-gradient(#d8ccd9,#bfb0c7)}
.search-row{display:flex;gap:4px}
.search-row .field{flex:1}
.search-row .go{width:40px;height:22px;margin:4px 0;background:var(--purple);color:#fff;font-size:10px;display:flex;align-items:center;justify-content:center}
.swatches{display:grid;grid-template-columns:repeat(6,1fr);gap:8px}
.swatches span{height:28px;border:1px solid var(--line)}
.info li{font-size:11px;padding:7px 4px 7px 14px;border-bottom:1px dotted var(--line);position:relative}
.info li::before{content:"";position:absolute;left:2px;top:12px;border-left:5px solid var(--lilac);border-top:4px solid transparent;border-bottom:4px solid transparent}
.promo.wrap{height:110px;background:linear-gradient(90deg,#fff,#f1e9f5)}
.promo.wrap b{font-size:22px;color:var(--pink)}

/* main */
.main{position:absolute;top:508px;left:360px;width:768px;display:flex;flex-direction:column;gap:20px}
.guarantee{height:170px;background:var(--white);border:1px solid var(--line);display:flex}
.guarantee .txt{width:440px;padding:14px 16px}
.guarantee h2{font-size:16px;color:var(--purple-dark);margin-bottom:2px}
.guarantee h2 em{font-style:normal;color:var(--pink);font-size:20px}
.guarantee .lead{font-size:11px;color:var(--muted);margin-bottom:8px}
.point{display:flex;align-items:center;gap:10px;margin:5px 0;font-size:12px}
.point i{font-style:normal;background:var(--purple);color:#fff;font-size:10px;padding:2px 8px}
.guarantee .img{flex:1;background:linear-gradient(120deg,#f3e6ee,#d9cbe2)}
.starter{height:60px;background:linear-gradient(90deg,#fff3e6,#ffe0c9);border:1px solid #f3c9a8;display:flex;align-items:center;justify-content:flex-end;padding-right:24px;gap:12px;position:relative}
.starter small{position:absolute;left:20px;top:10px;font-size:11px;color:var(--muted)}
.starter b{font-size:22px;color:var(--orange)}
.starter strong{font-size:26px;color:var(--pink)}
.sec-head{display:flex;justify-content:space-between;align-items:flex-end;border-bottom:2px solid var(--lilac);padding-bottom:4px;margin-bottom:10px}
.sec-head h2{font-family:"Playfair Display",serif;font-size:26px;font-weight:400;color:var(--purple-dark);line-height:1}
.sec-head span{font-size:10px;color:var(--muted)}
.topics{height:180px}
.topics li{display:flex;gap:20px;font-size:11px;padding:6px 4px;border-bottom:1px dotted var(--line)}
.topics time{color:var(--muted);width:60px}
.topics a{color:var(--purple);text-decoration:none}
.card .ph{background:linear-gradient(#efe6f2,#d9cce2);border:1px solid var(--line)}
.card p{font-size:10px;margin-top:4px;line-height:1.4}
.card .price{color:var(--pink);font-weight:700;font-size:11px}
.news{height:220px}
.carousel{display:flex;align-items:center;gap:10px}
.arrow{width:20px;height:60px;background:var(--lilac);color:#fff;display:flex;align-items:center;justify-content:center;font-size:12px}
.carousel .cards{flex:1;display:grid;grid-template-columns:repeat(5,1fr);gap:10px}
.news .ph{height:110px}
.pick{height:260px}
.pick .cards{display:grid;grid-template-columns:repeat(4,1fr);gap:16px}
.pick .ph{height:150px;background:linear-gradient(#f7e3ec,#e3d3ea)}
.pick .name{font-size:11px;font-weight:700;background:var(--lilac-soft);padding:3px 6px;margin-top:4px}
.rank{height:380px}
.tabs{display:flex;gap:2px;margin-bottom:12px}
.tabs span{flex:1;height:26px;background:var(--lilac-soft);font-size:11px;display:flex;align-items:center;justify-content:center;color:var(--purple-dark)}
.tabs span.on{background:var(--purple);color:#fff}
.rank .cards{display:grid;grid-template-columns:repeat(5,1fr);gap:12px}
.rank .badge{height:26px;background:var(--purple-dark);color:#fff;font-family:"Playfair Display",serif;font-size:14px;display:flex;align-items:center;justify-content:center;margin-bottom:4px}
.rank .ph{height:170px}
.voice{height:640px}
.voice-hero{height:90px;background:linear-gradient(90deg,#fff 50%,#e5dae9);border:1px solid var(--line);display:flex;align-items:center;padding-left:16px;font-size:12px;color:var(--ink);margin-bottom:10px}
.voice-item{display:flex;gap:12px;padding:10px;border-bottom:1px dotted var(--line);background:var(--white);height:86px}
.voice-item .av{width:40px;height:40px;border-radius:50%;background:var(--lilac-soft);flex:none}
.voice-item h3{font-size:12px;color:var(--pink)}
.voice-item p{font-size:10px;color:var(--ink)}
.voice-item:nth-child(even){background:var(--lilac-pale)}
.btn-more{width:200px;height:30px;margin:10px 0 0 auto;background:var(--pink);color:#fff;font-size:11px;display:flex;align-items:center;justify-content:center;border-radius:2px}
.widgets{height:560px;display:flex;gap:20px}
.widget{flex:1;background:var(--white);border:1px solid var(--line)}
.widget .wh{height:40px;background:var(--lilac-soft);display:flex;align-items:center;padding:0 10px;font-size:13px;font-weight:700;color:var(--purple-dark)}
.feed li{display:flex;gap:8px;padding:10px;border-bottom:1px solid var(--lilac-soft);height:72px}
.feed .av{width:36px;height:36px;background:var(--lilac);flex:none}
.feed p{font-size:10px}
.fans{display:grid;grid-template-columns:repeat(5,1fr);gap:8px;padding:10px}
.fans span{height:50px;background:var(--lilac-soft)}

/* footer */
.totop{position:absolute;top:3150px;right:72px;width:140px;height:26px;background:var(--purple);color:#fff;font-size:11px;display:flex;align-items:center;justify-content:center}
.flinks{position:absolute;top:3176px;left:0;width:1200px;height:40px;background:var(--lilac-soft);display:flex;align-items:center;justify-content:center;gap:24px;font-size:11px;color:var(--purple-dark)}
.footer{position:absolute;top:3216px;left:0;width:1200px;height:1004px;background:var(--purple-dark);color:#e6def0}
.footer .brand{color:#fff;top:40px}
.footer .addr{position:absolute;left:72px;top:100px;font-size:11px;line-height:1.8;width:300px}
.fcol{position:absolute;top:40px;width:200px;font-size:11px;line-height:2}
.fcol h4{font-size:12px;color:#fff;border-bottom:1px solid #6b5b85;margin-bottom:6px}
.copy{position:absolute;top:4220px;left:0;width:1200px;height:60px;background:#2f2542;color:#b9accb;font-size:10px;display:flex;align-items:center;justify-content:center}
</style>
</head>
<body>

<header class="header">
  <p class="tagline">バレエ用品・レオタード・シューズの専門通販サイト キラヴォ</p>
  <div class="brand"><span class="dot"></span>Kiravo</div>
  <p class="hours">受付時間 平日10:00〜18:00<br>土日祝日はお休みです</p>
  <div class="phone">
    <svg width="26" height="26" viewBox="0 0 24 24"><path d="M6.6 10.8a15 15 0 0 0 6.6 6.6l2.2-2.2a1 1 0 0 1 1-.25 11 11 0 0 0 3.6.6 1 1 0 0 1 1 1V20a1 1 0 0 1-1 1A17 17 0 0 1 3 4a1 1 0 0 1 1-1h3.5a1 1 0 0 1 1 1c0 1.25.2 2.45.6 3.6a1 1 0 0 1-.25 1z" fill="#5a4777"/></svg>
    0120-417-260
  </div>
  <p class="util">ログイン ｜ お問い合わせ</p>
  <div class="btn-cart">カートを見る</div>
  <div class="btn-shop">商品を見る ▶</div>
</header>

<section class="hero" role="img" aria-label="バレエスタジオで座るバレリーナの写真">
  <h1>キラヴォへようこそ</h1>
  <p>バレエ経験者のスタッフが厳選した商品をセレクト<br>初心者から本格派まで使えるバレエショップです</p>
</section>

<nav class="gnav">
  <ul>
    <li>バレエ用品の購入</li><li>初めての方へ</li><li>ご利用ガイド</li><li>商品一覧</li><li>お客様の声</li><li>よくあるご質問</li>
  </ul>
</nav>

<aside class="side">
  <div class="box" style="height:130px">
    <div class="box-head">会員ログイン<small>Member login</small></div>
    <div class="box-body">
      <div class="field">メールアドレス</div>
      <div class="field">パスワード</div>
      <div class="btn-sm">ログインする</div>
    </div>
  </div>
  <div class="promo member"><b>お得な会員特典</b><span>必要なお買い物でポイントがたまる</span></div>
  <div class="promo staff"><div class="img" role="img" aria-label="笑顔のスタッフの写真"></div><b>専門スタッフが<br>誠実・丁寧に</b><span>お答えします</span></div>
  <div class="box" style="height:90px">
    <div class="box-head">商品検索<small>Search</small></div>
    <div class="box-body"><div class="search-row"><div class="field">キーワードを入力</div><div class="go">検索</div></div></div>
  </div>
  <div class="box" style="height:140px">
    <div class="box-head">カラーで探す<small>Color</small></div>
    <div class="box-body"><div class="swatches">
      <span style="background:#111"></span><span style="background:#6b6b6b"></span><span style="background:#c9c9c9"></span><span style="background:#fff"></span><span style="background:#f6c9d6"></span><span style="background:#e7b6c8"></span>
      <span style="background:#c7a6d9"></span><span style="background:#8e6fae"></span><span style="background:#9fc4e6"></span><span style="background:#b9e0c7"></span><span style="background:#f7e6a6"></span><span style="background:#c83a4a"></span>
    </div></div>
  </div>
  <div class="box" style="height:170px">
    <div class="box-head">メールマガジン<small>Mail magazine</small></div>
    <div class="box-body">
      <p class="row-label">新商品やセールの情報をいち早くお届けします。</p>
      <div class="field">メールアドレス</div>
      <div class="btn-sm">メルマガ登録</div>
      <p class="link-sm">解除はこちら</p>
    </div>
  </div>
  <div class="box" style="height:260px">
    <div class="box-head">お知らせ・案内<small>Information</small></div>
    <ul class="box-body info">
      <li>特定商取引法表記</li><li>お支払い方法について</li><li>配送方法について</li><li>返品・交換について</li><li>メールが届かない方へ</li><li>バレエ用語解説</li><li>お客様情報について</li>
    </ul>
  </div>
  <div class="promo wrap"><span style="font-size:12px">大切な人へのギフトに</span><b>無料ラッピング</b><span style="font-size:12px">サービス実施中</span></div>
</aside>

<main class="main">
  <section class="guarantee">
    <div class="txt">
      <h2>Kiravoは<em>3つの保証</em>をお約束</h2>
      <p class="lead">安心してお買い物いただけます。</p>
      <div class="point"><i>Point1</i>安心の商品・品質保証</div>
      <div class="point"><i>Point2</i>全商品7日間の返品保証</div>
      <div class="point"><i>Point3</i>初回交換の送料無料</div>
    </div>
    <div class="img" role="img" aria-label="レオタード姿の子どもたちの写真"></div>
  </section>

  <section class="starter"><small>初心者の方に嬉しいセット</small><b>バレエスターターセット</b><strong>500円引き</strong></section>

  <section class="topics">
    <div class="sec-head"><h2>Topics</h2><span>トピックス</span></div>
    <ul>
      <li><time>7月5日</time><a>新商品のレオタードが入荷しました</a></li>
      <li><time>7月2日</time><a>新商品のバレエシューズを販売開始しました</a></li>
      <li><time>6月28日</time><a>夏のセール開催のお知らせ</a></li>
      <li><time>6月20日</time><a>新商品のスカートを販売開始しました</a></li>
      <li><time>6月12日</time><a>ラッピングサービスを開始しました</a></li>
    </ul>
  </section>

  <section class="news">
    <div class="sec-head"><h2>What's new</h2><span>新着情報</span></div>
    <div class="carousel">
      <div class="arrow">◀</div>
      <div class="cards">
        <div class="card"><div class="ph" role="img" aria-label="新着レオタード商品の写真"></div><p>キャミソールレオタード ラベンダー</p></div>
        <div class="card"><div class="ph" role="img" aria-label="新着レオタード商品の写真"></div><p>キャミソールレオタード ピンク</p></div>
        <div class="card"><div class="ph" role="img" aria-label="新着レオタード商品の写真"></div><p>半袖レオタード ブルー</p></div>
        <div class="card"><div class="ph" role="img" aria-label="新着レオタード商品の写真"></div><p>半袖レオタード ホワイト</p></div>
        <div class="card"><div class="ph" role="img" aria-label="新着レオタード商品の写真"></div><p>スカート付きレオタード</p></div>
      </div>
      <div class="arrow">▶</div>
    </div>
  </section>

  <section class="pick">
    <div class="sec-head"><h2>Pick up</h2><span>ピックアップ商品</span></div>
    <div class="cards">
      <div class="card"><div class="ph" role="img" aria-label="ピンクのレオタードの写真"></div><p class="name">袖スカート付レオタード</p><p>柔らかな素材で動きやすい</p></div>
      <div class="card"><div class="ph" role="img" aria-label="水色のレオタードの写真"></div><p class="name">袖スカート付レオタード</p><p>発表会にもおすすめです</p></div>
      <div class="card"><div class="ph" role="img" aria-label="紫のレオタードの写真"></div><p class="name">袖スカート付レオタード</p><p>お子様に人気のデザイン</p></div>
      <div class="card"><div class="ph" role="img" aria-label="白のレオタードの写真"></div><p class="name">袖スカート付レオタード</p><p>シンプルで合わせやすい</p></div>
    </div>
  </section>

  <section class="rank">
    <div class="sec-head"><h2>Ranking</h2><span>売上ランキング</span></div>
    <div class="tabs"><span class="on">子供レオタード</span><span>大人レオタード</span><span>ウォームアップ</span><span>バレエシューズ</span><span>タイツ</span><span>レッスン用品</span></div>
    <div class="cards">
      <div class="card"><div class="badge">No.1</div><div class="ph" role="img" aria-label="1位の子供用レオタードの写真"></div><p>子供用フレンチスカート付レオタード</p><p class="price">3,990円</p></div>
      <div class="card"><div class="badge">No.2</div><div class="ph" role="img" aria-label="2位の子供用レオタードの写真"></div><p>子供用フレンチスカート付レオタード</p><p class="price">3,990円</p></div>
      <div class="card"><div class="badge">No.3</div><div class="ph" role="img" aria-label="3位の子供用レオタードの写真"></div><p>子供用フレンチスカート付レオタード</p><p class="price">3,990円</p></div>
      <div class="card"><div class="badge">No.4</div><div class="ph" role="img" aria-label="4位の子供用レオタードの写真"></div><p>子供用フレンチスカート付レオタード</p><p class="price">3,990円</p></div>
      <div class="card"><div class="badge">No.5</div><div class="ph" role="img" aria-label="5位の子供用レオタードの写真"></div><p>子供用フレンチスカート付レオタード</p><p class="price">3,990円</p></div>
    </div>
  </section>

  <section class="voice">
    <div class="sec-head"><h2>Customer's Voice</h2><span>お客様の喜びの声</span></div>
    <div class="voice-hero" role="img" aria-label="レッスン中の女の子の写真">ご利用いただいたお客様から、たくさんの嬉しい声をいただきました。</div>
    <div class="voice-item"><span class="av"></span><div><h3>いい商品です！</h3><p>子供が初めてのレオタードを選ぶ時に丁寧に教えてもらえました。サイズもぴったりで、とても喜んでいます。また利用したいです。</p></div></div>
    <div class="voice-item"><span class="av"></span><div><h3>とても気に入りました</h3><p>届いてすぐにレッスンで着ました。色がとてもきれいで、生地もしっかりしています。先生にも褒めてもらえました。</p></div></div>
    <div class="voice-item"><span class="av"></span><div><h3>とても安心できます</h3><p>初めてのバレエ用品でしたが、スタッフの方の説明が分かりやすく、安心して購入できました。発送も早かったです。</p></div></div>
    <div class="voice-item"><span class="av"></span><div><h3>満足です！</h3><p>サイズ交換にも丁寧に対応していただきました。梱包もきれいで、プレゼントにもぴったりでした。ありがとうございました。</p></div></div>
    <div class="voice-item"><span class="av"></span><div><h3>良い買い物でした</h3><p>バレエシューズとタイツをまとめて購入しました。品質も良く、値段も手頃で満足しています。次回もお願いします。</p></div></div>
    <div class="btn-more">他のお客様の声を見る ▶</div>
  </section>

  <section class="widgets">
    <div class="widget">
      <div class="wh">ファンページ</div>
      <div class="fans">
        <span></span><span></span><span></span><span></span><span></span>
        <span></span><span></span><span></span><span></span><span></span>
      </div>
      <ul class="feed">
        <li><span class="av"></span><p>キラヴォ<br>新しいレオタードが入荷しました。ぜひご覧ください。</p></li>
        <li><span class="av"></span><p>キラヴォ<br>夏のセールを開催中です。お見逃しなく。</p></li>
      </ul>
    </div>
    <div class="widget">
      <div class="wh">つぶやき</div>
      <ul class="feed">
        <li><span class="av"></span><p>キラヴォ<br>新商品のバレエシューズを販売開始しました。</p></li>
        <li><span class="av"></span><p>キラヴォ<br>本日の発送は終了しました。明日もお待ちしています。</p></li>
        <li><span class="av"></span><p>キラヴォ<br>発表会用のスカートが人気です。</p></li>
        <li><span class="av"></span><p>キラヴォ<br>ラッピングサービスを始めました。</p></li>
        <li><span class="av"></span><p>キラヴォ<br>メルマガ会員限定のクーポン配信中。</p></li>
        <li><span class="av"></span><p>キラヴォ<br>新色のタイツが入荷しました。</p></li>
      </ul>
    </div>
  </section>
</main>

<div class="totop">ページの先頭へ ▲</div>
<div class="flinks"><span>トップページ</span><span>バレエ用品の購入</span><span>初めての方へ</span><span>ご利用ガイド</span><span>商品一覧</span><span>お客様の声</span><span>よくあるご質問</span><span>会社概要</span></div>

<footer class="footer">
  <div class="brand"><span class="dot"></span>Kiravo</div>
  <p class="addr">バレエ用品・レオタード通販<br>〒000-0000 東京都架空区見本町1-2-3<br>TEL 0120-417-260<br>www.kiravostore.com</p>
  <div class="fcol" style="left:420px"><h4>ご利用ガイド</h4>ご注文方法<br>お支払い方法<br>配送について<br>返品・交換</div>
  <div class="fcol" style="left:640px"><h4>商品カテゴリ</h4>子供レオタード<br>大人レオタード<br>バレエシューズ<br>タイツ<br>レッスン用品</div>
  <div class="fcol" style="left:860px;width:268px"><h4>コンテンツ</h4>初めての方へ<br>お客様の声<br>よくあるご質問<br>会社概要<br>お問い合わせ</div>
</footer>
<div class="copy">Copyright © Kiravo. All Rights Reserved.</div>

</body>
</html>
```